Consultant Firm Marketing Flyer

I want to use this flyer to market health care consultant services. I would like a front and back glossy, professional, yet bold and eye catching design. I would like it to convey knowledge, expertise, partnership and strength. The colors should blue and white but I am very open to the designer being creative. You can visit my website to see colors and images I want to use at brightharborcare.net
I would like the home page image on my website to be incorporated into the flyer but I am also open to other images that work with the design. The designer can be creative.

I want to highlight 4 service area’s of focus to my clients:
1. Revenue Cycle Optimization (making my clients money)
2. Practice Management Optimization (improving clinical operations)
3. Health Compliance (following the law)
4. Health Care Technology: (Telemedicine and AI)
Please be creative. Go where ever your creativity leads.

```html
<!DOCTYPE html>
<html lang="en">
<head>
<meta charset="utf-8">
<title>Bright Harbor Health Partners – Flyer</title>
<link href="https://fonts.googleapis.com/css2?family=Montserrat:wght@300;400;600&family=Open+Sans:wght@400;600;700&family=Roboto+Condensed:wght@300;400;700&display=swap" rel="stylesheet">
<style>
  :root{
    --bg:#e4e6ea;
    --paper:#ffffff;
    --paper-tint:#f4f6f9;
    --blue:#1f86cc;
    --sky:#3aa3db;
    --navy:#17427e;
    --ink:#2f3640;
    --muted:#6b7480;
    --photo-a:#c9cfd6;
    --photo-b:#8e9aa8;
  }
  *{box-sizing:border-box;margin:0;padding:0}
  html,body{width:1200px;height:776px;overflow:hidden}
  body{background:var(--bg);font-family:"Open Sans",sans-serif;color:var(--ink);position:relative}
  .page{position:absolute;top:20px;width:520px;height:736px;background:var(--paper);box-shadow:0 2px 8px rgba(0,0,0,.15);overflow:hidden}
  .page--front{left:60px}
  .page--back{left:620px;background:linear-gradient(180deg,var(--paper),var(--paper-tint))}

  /* brand */
  .brand{position:absolute;font-family:"Open Sans",sans-serif;color:var(--navy);font-weight:700;display:flex;align-items:center;gap:8px;white-space:nowrap}
  .brand__dot{width:12px;height:12px;border-radius:50%;background:var(--navy)}
  .page--front .brand{left:24px;top:34px;font-size:15px}
  .page--back .brand{right:24px;top:30px;font-size:12px}

  .call-us{position:absolute;right:28px;top:30px;display:flex;align-items:center;gap:10px;color:var(--navy);white-space:nowrap}
  .call-us__label{font-family:"Montserrat",sans-serif;font-weight:300;font-size:15px;color:var(--sky);letter-spacing:.5px}
  .call-us__number{font-weight:700;font-size:16px}

  /* front photos */
  .photo{position:absolute;background:linear-gradient(135deg,var(--photo-a),var(--photo-b))}
  .photo--team{left:0;top:96px;width:520px;height:250px}
  .photo-wave{position:absolute;left:0;top:276px;width:520px;height:80px}
  .headline-box{position:absolute;right:0;top:108px;width:190px;height:118px;background:var(--paper);padding:18px 16px;font-family:"Montserrat",sans-serif;font-weight:300;font-size:22px;line-height:1.15;color:var(--navy);letter-spacing:.5px}
  .photo--doctors{left:340px;top:250px;width:176px;height:222px;border:6px solid var(--paper);background:linear-gradient(160deg,#a9c6da,#e9eef2 55%,#7d8a98)}

  .welcome{position:absolute;left:26px;top:400px;font-family:"Montserrat",sans-serif;color:var(--blue)}
  .welcome__intro{font-weight:300;font-size:28px;display:block}
  .welcome__name{font-weight:600;font-size:31px;line-height:1.2;display:block}
  .intro-text{position:absolute;left:26px;top:520px;width:470px;font-size:10.6px;line-height:1.45;color:var(--navy)}
  .info-bar{position:absolute;left:26px;top:662px;width:470px;height:40px;padding:0 8px;border:2px solid var(--blue);display:flex;align-items:center;justify-content:center;gap:5px;font-family:"Roboto Condensed",sans-serif;color:var(--blue);font-weight:300;font-size:10.5px;white-space:nowrap}
  .info-bar strong{color:var(--navy);font-weight:700;font-size:12.5px}

  /* back */
  .services-title{position:absolute;left:30px;top:52px;font-family:"Montserrat",sans-serif;font-weight:600;font-size:24px;color:var(--sky);letter-spacing:.5px;padding-bottom:6px;border-bottom:2px solid var(--sky)}
  .services{position:absolute;left:20px;top:110px;width:480px;display:grid;grid-template-columns:1fr 1fr;row-gap:30px;column-gap:20px}
  .service{text-align:center}
  .service__title{font-family:"Roboto Condensed",sans-serif;font-weight:700;font-size:13px;color:var(--blue);text-transform:uppercase;white-space:nowrap}
  .service__tag{font-family:"Roboto Condensed",sans-serif;font-weight:300;font-size:10px;color:var(--muted);text-transform:uppercase;margin-top:2px;white-space:nowrap}
  .service__icon{width:60px;height:60px;margin:12px auto}
  .service__text{font-size:10px;line-height:1.45;color:var(--muted);padding:0 10px}
  .footer-rule{position:absolute;left:30px;right:30px;top:620px;border-top:2px solid var(--sky)}
  .contacts{position:absolute;left:30px;right:24px;top:640px;display:flex;justify-content:space-between}
  .contact{display:flex;align-items:center;gap:7px;padding-right:6px;white-space:nowrap}
  .contact + .contact{border-left:1px solid #d5dbe2;padding-left:10px}
  .contact__label{font-family:"Roboto Condensed",sans-serif;font-weight:300;font-size:10px;color:var(--muted);text-transform:uppercase;display:block}
  .contact__value{font-weight:700;font-size:10px;color:var(--navy);display:block}
</style>
</head>
<body>

<section class="page page--front">
  <div class="brand"><span class="brand__dot"></span>Bright Harbor Health Partners LLC</div>
  <div class="call-us">
    <svg width="26" height="26" viewBox="0 0 24 24" aria-hidden="true"><path fill="#17427e" d="M6.6 10.8a15 15 0 0 0 6.6 6.6l2.2-2.2c.3-.3.7-.4 1-.2 1.1.4 2.3.6 3.6.6.6 0 1 .4 1 1V20c0 .6-.4 1-1 1A17 17 0 0 1 3 4c0-.6.4-1 1-1h3.5c.6 0 1 .4 1 1 0 1.3.2 2.5.6 3.6.1.3 0 .7-.2 1z"/></svg>
    <div><div class="call-us__label">CALL US</div><div class="call-us__number">(555) 214-0377</div></div>
  </div>

  <div class="photo photo--team" role="img" aria-label="Photo of a team of doctors and consultants meeting around a table"></div>
  <svg class="photo-wave" viewBox="0 0 520 80" preserveAspectRatio="none" aria-hidden="true"><path d="M0 20 C140 60 260 70 520 30 L520 80 L0 80 Z" fill="#fff"/></svg>
  <div class="headline-box">ADVANCING HEALTHCARE OPERATIONS</div>
  <div class="photo photo--doctors" role="img" aria-label="Photo of a smiling doctor holding a tablet with colleagues behind"></div>

  <h1 class="welcome"><span class="welcome__intro">Welcome to</span><span class="welcome__name">Bright Harbor<br>Health Partners</span></h1>
  <p class="intro-text">Bright Harbor Health Partners (BHP) is a healthcare consulting firm skilled at helping physician practices advance their strategic vision in an ever-evolving healthcare system. Bright Harbor Health Partners specializes in revenue cycle optimization, practice management improvement and developing new physician practices. Our technical skills allow us to dig deep into your revenue cycle while our strategic approach ensures we're keeping our eyes on the entire financial picture.</p>
  <div class="info-bar">FOR MORE INFO CALL US ON <strong>(555) 214-0377</strong> OR VISIT US AT <strong>WWW.BRIGHTHARBORCARE.NET</strong></div>
</section>

<section class="page page--back">
  <h2 class="services-title">OUR SERVICES</h2>
  <div class="brand"><span class="brand__dot"></span>Bright Harbor Health Partners LLC</div>

  <div class="services">
    <article class="service">
      <h3 class="service__title">Revenue Cycle Optimization</h3>
      <p class="service__tag">(Making my clients money)</p>
      <svg class="service__icon" viewBox="0 0 60 60" aria-hidden="true"><g fill="none" stroke="#3aa3db" stroke-width="6"><path d="M14 22a18 18 0 0 1 28-6"/><path d="M48 30a18 18 0 0 1-10 16"/><path d="M24 47a18 18 0 0 1-12-12"/></g><g fill="#3aa3db"><path d="M40 8l8 10-12 2z"/><path d="M44 50l-12 1 6-10z"/><path d="M6 36l8-8 4 11z"/></g></svg>
      <p class="service__text">In today's increasingly complex health care environment it's important now more than ever that medical practices closely manage their revenue cycle. Bright Harbor Health Partners (BHP) understands the reimbursement landscape</p>
    </article>
    <article class="service">
      <h3 class="service__title">Health Regulatory Compliance</h3>
      <p class="service__tag">(Following the law)</p>
      <svg class="service__icon" viewBox="0 0 60 60" aria-hidden="true"><path d="M12 8h34v40a6 6 0 0 1-6 6H18a6 6 0 0 0 6-6V14h-12z" fill="#3aa3db"/><path d="M36 22l8 3v7c0 5-4 8-8 10-4-2-8-5-8-10v-7z" fill="#fff"/><path d="M32 31l3 3 5-6" stroke="#3aa3db" stroke-width="2.5" fill="none"/></svg>
      <p class="service__text">In a heavily regulated healthcare environment medical practices need to be acutely aware of regulations as they present huge liabilities. It is extremely important to ensure compliance with regulations. BHP offers a host of comprehensive compliance services.</p>
    </article>
    <article class="service">
      <h3 class="service__title">Practice Management Optimization</h3>
      <p class="service__tag">(Improving clinical operations)</p>
      <svg class="service__icon" viewBox="0 0 60 60" aria-hidden="true"><circle cx="30" cy="16" r="7" fill="none" stroke="#3aa3db" stroke-width="5" stroke-dasharray="4 2"/><path d="M6 24l6 16 10 8v8h-6v-6L6 42zM54 24l-6 16-10 8v8h6v-6l10-8z" fill="#3aa3db"/></svg>
      <p class="service__text">Practice Management is challenging and it requires the right balance of skill, knowledge, experience and management expertise. BHP offers assessment and optimization in Patient Access &amp; Scheduling, Patient Experience, Staff Experience</p>
    </article>
    <article class="service">
      <h3 class="service__title">Human Resource Management</h3>
      <p class="service__tag">(Development of policies &amp; procedures)</p>
      <svg class="service__icon" viewBox="0 0 60 60" aria-hidden="true"><circle cx="30" cy="24" r="17" fill="none" stroke="#3aa3db" stroke-width="6" stroke-dasharray="6 3"/><circle cx="30" cy="20" r="5" fill="#3aa3db"/><path d="M21 34a9 8 0 0 1 18 0z" fill="#3aa3db"/><path d="M8 44h12l8 6h16v6H26l-8-4H8z" fill="#3aa3db"/></svg>
      <p class="service__text">Do you need Human Resources Management but don't want the expense of a full service Human Resources Department? Not having a full service Human Resources Department can increase liability and be costly to your medical practice.</p>
    </article>
  </div>

  <div class="footer-rule"></div>
  <div class="contacts">
    <div class="contact">
      <svg width="18" height="18" viewBox="0 0 24 24" aria-hidden="true"><path fill="#3aa3db" d="M6.6 10.8a15 15 0 0 0 6.6 6.6l2.2-2.2c.3-.3.7-.4 1-.2 1.1.4 2.3.6 3.6.6.6 0 1 .4 1 1V20c0 .6-.4 1-1 1A17 17 0 0 1 3 4c0-.6.4-1 1-1h3.5c.6 0 1 .4 1 1 0 1.3.2 2.5.6 3.6.1.3 0 .7-.2 1z"/></svg>
      <div><span class="contact__label">Call us</span><span class="contact__value">(555) 214-0377</span></div>
    </div>
    <div class="contact">
      <svg width="24" height="18" viewBox="0 0 26 20" aria-hidden="true"><rect x="1" y="2" width="24" height="16" fill="#3aa3db"/><path d="M1 2l12 9 12-9" fill="none" stroke="#fff" stroke-width="2"/></svg>
      <div><span class="contact__label">Email us</span><span class="contact__value">info@brightharborcare.net</span></div>
    </div>
    <div class="contact">
      <svg width="20" height="20" viewBox="0 0 24 24" aria-hidden="true"><g fill="none" stroke="#3aa3db" stroke-width="1.8"><circle cx="12" cy="12" r="10"/><ellipse cx="12" cy="12" rx="4.5" ry="10"/><path d="M2 12h20M4 6.5h16M4 17.5h16"/></g></svg>
      <div><span class="contact__label">Visit us</span><span class="contact__value">www.brightharborcare.net</span></div>
    </div>
  </div>
</section>

</body>
</html>
```